Calvin Pruett Insurance Biz Card
Biz card and stationary
Calvin Pruett Insurance Biz Card - Financial Services
Creative Brief
Professional
Calvin Pruett
Independent Agent
Millbrook, NC
pruettgroup@lanvex.example.net
www.calvinpruettinsurance.example.com
please use the logo we upload, and keep all font at a size 9 or 10.
please use the content we upload for an example of the back of the card

```html
<!DOCTYPE html>
<html lang="en">
<head>
<meta charset="utf-8">
<title>Calvin Pruett Insurance – Business Card</title>
<link rel="stylesheet" href="https://fonts.googleapis.com/css2?family=Tinos:wght@400;700&display=swap">
<style>
  :root {
    --navy: #1c2b5e;
    --white: #ffffff;
    --stone: #a8a69b;
    --backdrop: #e9e8e4;
    --card-shadow: rgba(0, 0, 0, 0.18);
  }
  html, body {
    margin: 0;
    padding: 0;
    width: 1200px;
    height: 778px;
    overflow: hidden;
    background: var(--backdrop);
  }
  .card {
    position: absolute;
    left: 60px;
    top: 78px;
    width: 1080px;
    height: 621px;
    background: var(--navy);
    box-shadow: 0 6px 18px var(--card-shadow);
    overflow: hidden;
    font-family: "Tinos", "Times New Roman", serif;
  }
  .card-shapes {
    position: absolute;
    inset: 0;
    width: 100%;
    height: 100%;
  }
  .brand {
    position: absolute;
    left: 66px;
    top: 225px;
    display: flex;
    align-items: center;
    gap: 18px;
  }
  .brand-square {
    width: 123px;
    height: 132px;
    background: var(--navy);
  }
  .brand-name {
    margin: 0;
    color: var(--navy);
    font-size: 38px;
    font-weight: 400;
    line-height: 1.05;
  }
  .agent {
    position: absolute;
    right: 84px;
    top: 118px;
    text-align: right;
    color: var(--white);
  }
  .agent-name {
    margin: 0;
    font-size: 36px;
    font-weight: 700;
    line-height: 1.1;
  }
  .agent-title {
    margin: 6px 0 0;
    font-size: 27px;
    line-height: 1.1;
  }
  .contact {
    position: absolute;
    right: 84px;
    top: 366px;
    margin: 0;
    padding: 0;
    list-style: none;
    color: var(--white);
    font-size: 24px;
    line-height: 1;
    text-align: right;
  }
  .contact li {
    display: flex;
    justify-content: flex-end;
    align-items: center;
    gap: 14px;
    height: 34px;
  }
  .contact .city {
    margin-bottom: 20px;
  }
  .contact-icon {
    width: 20px;
    height: 20px;
    flex: none;
  }
</style>
</head>
<body>
  <article class="card">
    <svg class="card-shapes" viewBox="0 0 1080 621" preserveAspectRatio="none" aria-hidden="true">
      <path d="M0,0 H510 C640,80 672,220 632,340 C582,490 380,592 150,621 H0 Z" fill="var(--stone)"/>
      <path d="M0,0 H480 C600,60 642,200 604,330 C552,482 330,592 90,621 H0 Z" fill="var(--white)"/>
    </svg>

    <div class="brand">
      <div class="brand-square"></div>
      <p class="brand-name">Calvin Pruett<br>Insurance, LLC</p>
    </div>

    <header class="agent">
      <h1 class="agent-name">Calvin Pruett</h1>
      <p class="agent-title">Independent Agent</p>
    </header>

    <ul class="contact">
      <li class="city">Millbrook, NC</li>
      <li>336-555-0148
        <svg class="contact-icon" viewBox="0 0 24 24" aria-label="phone"><path d="M7 4c1 0 2 3 2 4s-2 1-2 2c1 3 3 5 6 6 1 0 1-2 2-2s4 1 4 2-2 4-4 4C10 20 4 14 4 8c0-2 2-4 3-4z" fill="var(--white)"/></svg>
      </li>
      <li>pruettgroup@lanvex.example.net
        <svg class="contact-icon" viewBox="0 0 24 24" aria-label="email"><rect x="3" y="6" width="18" height="12" fill="none" stroke="var(--white)" stroke-width="2"/><path d="M3 6l9 7 9-7" fill="none" stroke="var(--white)" stroke-width="2"/></svg>
      </li>
      <li>www.calvinpruettinsurance.example.com
        <svg class="contact-icon" viewBox="0 0 24 24" aria-label="website"><circle cx="12" cy="12" r="9" fill="var(--white)"/><path d="M12 3c-3 3-3 15 0 18M12 3c3 3 3 15 0 18M3 12h18" fill="none" stroke="var(--navy)" stroke-width="1.5"/></svg>
      </li>
    </ul>
  </article>
</body>
</html>
```